Powerpoint presentation about personal finance

Investing 4$ per day is what has been required to become a millionaire by investing in the stock market from 1965 to 2015. Yet only 1% of the population is millionaire. This presentation is about the most common causes why people do not build significant wealth through their life. We intend to educate people with this presentation, but also build trust so they become client of our wealth management firm. Feel free to send us any question about this project.
Updates

Reason: I have uploaded the logo source file and an updated PPT file. Thanks

Target Market(s)

People with a willingness to save money between the age of 20 to 50 years old

Industry/Entity Type

Finance

Font styles to use
Sans Serif

Requirements
Must have
• We are looking at uniforming the design throughout the presentation with nice, classic tone colors, large font size as it needs to be visible 3 meters apart. The content of the presentation will be updated regularly.
Should not have
• cartoon style, not serious

```html
<!DOCTYPE html>
<html lang="fr">
<head>
<meta charset="utf-8">
<title>Slide – Investissement fixe</title>
<link href="https://fonts.googleapis.com/css2?family=Roboto+Condensed:wght@400;700&family=Roboto:wght@400&display=swap" rel="stylesheet">
<style>
  :root {
    --brand-blue: #0066b3;
    --brand-green: #00a651;
    --chart-blue: #1b8be6;
    --pin-dark: #262626;
    --text-dark: #444444;
    --axis-text: #555555;
    --grid: #eeeeee;
    --axis: #d6d6d6;
    --white: #ffffff;
  }
  * { margin: 0; padding: 0; box-sizing: border-box; }
  html, body { width: 1200px; height: 900px; overflow: hidden; background: var(--white); }
  .slide { position: relative; width: 1200px; height: 900px; background: var(--white); overflow: hidden; }

  .slide-header {
    position: absolute; top: 0; left: 0; width: 100%; height: 99px;
    background: var(--brand-blue);
    display: flex; align-items: center; justify-content: space-between;
    padding: 0 20px 0 24px;
  }
  .slide-title {
    font-family: "Roboto Condensed", sans-serif; font-weight: 700;
    font-size: 42px; color: var(--white); letter-spacing: 0.2px;
  }
  .brand {
    display: flex; align-items: center; gap: 12px;
    font-family: "Roboto Condensed", sans-serif; font-weight: 700;
    font-size: 22px; color: var(--white);
  }
  .brand-dot {
    width: 70px; height: 70px; border-radius: 50%;
    background: var(--white);
  }

  .growth-chart { position: absolute; left: 0; top: 150px; width: 810px; height: 668px; }
  .axis-label { font-family: "Roboto", sans-serif; font-size: 11px; fill: var(--axis-text); }

  .chart-note {
    position: absolute; left: 856px; top: 236px; width: 300px;
    font-family: "Roboto Condensed", sans-serif; font-weight: 400;
    font-size: 28px; line-height: 60px; color: var(--text-dark);
  }

  .slide-footer {
    position: absolute; left: 0; bottom: 0; width: 100%; height: 47px;
    background: var(--brand-green);
    display: flex; align-items: center; justify-content: space-between;
    padding: 0 14px 0 12px;
    font-family: "Roboto Condensed", sans-serif; font-weight: 700;
    font-size: 18px; color: var(--white);
  }
</style>
</head>
<body>
<main class="slide">
  <header class="slide-header">
    <h1 class="slide-title">PROJECT TITLE HERE</h1>
    <div class="brand"><span class="brand-name">Veltrosa Finance</span><span class="brand-dot"></span></div>
  </header>

  <svg class="growth-chart" viewBox="0 100 540 445" aria-label="Graphique de croissance de l'investissement">
    <g class="grid" stroke="var(--grid)" stroke-width="1">
      <line x1="62" y1="197" x2="503" y2="197"/>
      <line x1="62" y1="248" x2="503" y2="248"/>
      <line x1="62" y1="298" x2="503" y2="298"/>
      <line x1="62" y1="349" x2="503" y2="349"/>
      <line x1="62" y1="400" x2="503" y2="400"/>
      <line x1="62" y1="450" x2="503" y2="450"/>
    </g>
    <g class="axis" stroke="var(--axis)" stroke-width="1">
      <line x1="62" y1="501" x2="503" y2="501"/>
      <line x1="62" y1="501" x2="62" y2="506"/>
      <line x1="135" y1="501" x2="135" y2="506"/>
      <line x1="209" y1="501" x2="209" y2="506"/>
      <line x1="283" y1="501" x2="283" y2="506"/>
      <line x1="357" y1="501" x2="357" y2="506"/>
      <line x1="430" y1="501" x2="430" y2="506"/>
      <line x1="503" y1="501" x2="503" y2="506"/>
    </g>
    <g class="axis-label" text-anchor="end">
      <text x="48" y="201">60</text>
      <text x="48" y="252">50</text>
      <text x="48" y="302">40</text>
      <text x="48" y="353">30</text>
      <text x="48" y="404">20</text>
      <text x="48" y="454">10</text>
      <text x="48" y="505">0</text>
    </g>
    <g class="axis-label" text-anchor="middle">
      <text x="98" y="527">One</text>
      <text x="172" y="527">Two</text>
      <text x="246" y="527">Three</text>
      <text x="320" y="527">Four</text>
      <text x="393" y="527">Five</text>
      <text x="467" y="527">Six</text>
    </g>
    <polyline fill="none" stroke="var(--chart-blue)" stroke-width="4" stroke-linejoin="round"
      points="98,460 172,422 246,329 320,361 393,304 467,229"/>
    <g fill="var(--white)" stroke="var(--chart-blue)" stroke-width="3">
      <circle cx="98" cy="460" r="5"/>
      <circle cx="172" cy="422" r="5"/>
      <circle cx="246" cy="329" r="5"/>
      <circle cx="320" cy="361" r="5"/>
      <circle cx="393" cy="304" r="5"/>
      <circle cx="467" cy="229" r="5"/>
    </g>

    <g class="pin pin-start">
      <path d="M94,437 L72,415 A34,34 0 1 1 116,415 Z" fill="var(--pin-dark)"/>
      <g fill="var(--white)">
        <rect x="80" y="384" width="6" height="20"/>
        <path d="M88,384 L96,384 L99,372 Q102,368 104,372 L103,384 L110,384 Q113,385 112,389 L109,402 Q108,404 105,404 L88,404 Z"/>
      </g>
    </g>

    <g class="pin pin-peak">
      <path d="M466,209 L444,187 A34,34 0 1 1 488,187 Z" fill="var(--chart-blue)"/>
      <g fill="var(--white)" transform="rotate(45 466 162)">
        <path d="M466,144 Q474,152 474,164 L474,174 L458,174 L458,164 Q458,152 466,144 Z"/>
        <path d="M458,166 L452,178 L458,176 Z"/>
        <path d="M474,166 L480,178 L474,176 Z"/>
        <path d="M462,176 L470,176 L466,184 Z"/>
      </g>
      <circle cx="466" cy="160" r="3" fill="var(--chart-blue)"/>
    </g>
  </svg>

  <p class="chart-note">Investissement fixe<br>équivalent à 4$ par<br>jour dans les actions<br>pour un individu né en<br>1950 et qui a com-<br>mencé à épargner à 15<br>ans</p>

  <footer class="slide-footer">
    <span class="copyright">COPYRIGHT TEXT HERE</span>
    <span class="page-number">PAGE : 01</span>
  </footer>
</main>
</body>
</html>
```